Brume vodka

With the logo attached in the subsequent file, a business card that reflects a premium and organic vodka. On the first side, the company logo in large. The names must be included on the back of the card (Miguel Ángel Tomás Ferrandis with the number +34 655 271 389 and Pau Berenguer Casals and +34 677 314 920). The slogan "What binds us" and "Organic and permium vodka" in bold E-mail (brumevodka@mailfield.net); Website www.brumevodkaorg.net

```html
<!DOCTYPE html>
<html lang="en">
<head>
<meta charset="utf-8">
<title>Brume vodka – business card</title>
<link rel="stylesheet" href="https://fonts.googleapis.com/css2?family=Saira:wght@300;400;600&display=swap">
<style>
  :root {
    --canvas: #e4e4e4;
    --card: #ffffff;
    --ink: #8a8a8a;
    --ink-strong: #7a7a7a;
    --rule: #9a9a9a;
    --band-dark: #8e8e8e;
    --band-light: #c9c9c9;
    --on-band: #ffffff;
  }
  html, body {
    margin: 0;
    width: 1200px;
    height: 1000px;
    overflow: hidden;
    background: var(--canvas);
    font-family: "Saira", sans-serif;
  }
  .canvas { position: relative; width: 1200px; height: 1000px; }
  .card {
    position: absolute;
    width: 560px;
    height: 320px;
    background: var(--card);
    box-shadow: 0 6px 18px rgba(0,0,0,.18);
    overflow: hidden;
  }
  .card--front { left: 110px; top: 110px; }
  .card--back { left: 530px; top: 560px; }

  .wordmark {
    color: var(--ink);
    font-weight: 400;
    letter-spacing: 2px;
    margin: 0;
    white-space: nowrap;
  }
  .card--front .wordmark {
    position: absolute;
    left: 0; right: 0; top: 130px;
    text-align: center;
    font-size: 56px;
    line-height: 1;
  }
  .card--back .wordmark {
    position: absolute;
    right: 38px; top: 40px;
    font-size: 38px;
    line-height: 1;
  }
  .logo-rule {
    position: absolute;
    left: 190px; right: 30px; top: 100px;
    border-top: 1px solid var(--rule);
  }
  .slogan {
    position: absolute;
    right: 38px; top: 110px;
    margin: 0;
    text-align: right;
    color: var(--ink);
    font-weight: 600;
    font-size: 14px;
    line-height: 20px;
  }
  .names {
    position: absolute;
    left: 30px; top: 156px;
    margin: 0;
    color: var(--ink-strong);
    font-weight: 600;
    font-size: 16px;
    line-height: 21px;
    white-space: nowrap;
  }
  .names-rule {
    position: absolute;
    left: 30px; width: 270px; top: 204px;
    border-top: 1px solid var(--rule);
  }
  .contacts {
    position: absolute;
    left: 44px; top: 210px;
    margin: 0;
    color: var(--ink);
    font-weight: 300;
    font-size: 15px;
    line-height: 20px;
    white-space: nowrap;
  }
  .bands { position: absolute; left: 0; top: 0; }
  .website {
    position: absolute;
    right: 30px; top: 272px;
    margin: 0;
    color: var(--on-band);
    font-weight: 400;
    font-size: 15px;
    line-height: 20px;
  }
</style>
</head>
<body>
<main class="canvas">
  <section class="card card--front" aria-label="Card front">
    <p class="wordmark">Brume vodka</p>
  </section>

  <section class="card card--back" aria-label="Card back">
    <svg class="bands" width="560" height="320" viewBox="0 0 560 320" aria-hidden="true">
      <polygon points="0,307 560,307 560,320 0,320" fill="var(--band-light)"/>
      <polygon points="0,296 300,296 318,264 560,264 560,303 0,303" fill="var(--band-dark)"/>
    </svg>
    <p class="wordmark">Brume vodka</p>
    <div class="logo-rule"></div>
    <p class="slogan">What binds us<br>Organic and permium vodka</p>
    <p class="names">Miguel Ángel Tomás Ferrandis<br>Pau Berenguer Casals</p>
    <div class="names-rule"></div>
    <p class="contacts">+34 655 271 389<br>+34 677 314 920<br>brumevodka@mailfield.net</p>
    <p class="website">www.brumevodkaorg.net</p>
  </section>
</main>
</body>
</html>
```